" Fabricamos sapatos de luxo artesanalmente com os mínimos detalhes, divulgamos os modelos via Instagram, Facebook, Whatts Up, Ecommerce, Inicio de MicroFranquia para revenda direta. Parceria com Blogueiras e Venda Direta, entregamos via correios, pessoalmente. "

```html
<!DOCTYPE html>
<html lang="pt-BR">
<head>
<meta charset="UTF-8">
<title>Lia Montenegro — Tags</title>
<link href="https://fonts.googleapis.com/css2?family=Cinzel:wght@500&family=Cormorant+Garamond:wght@500&display=swap" rel="stylesheet">
<style>
  :root {
    --backdrop: #ecebe9;
    --tag-black: #111111;
    --ink-white: #f4f2ee;
    --gold: #c9a25a;
    --punch-hole: #ecebe9;
  }
  * { margin: 0; padding: 0; box-sizing: border-box; }
  html, body {
    width: 1200px;
    height: 1200px;
    overflow: hidden;
    background: var(--backdrop);
  }
  .sheet {
    position: relative;
    width: 1200px;
    height: 1200px;
  }
  .tag {
    position: absolute;
    width: 480px;
    height: 480px;
    border-radius: 50%;
    background: var(--tag-black);
    color: var(--ink-white);
  }
  .tag--front { left: 70px; top: 360px; }
  .tag--back { left: 650px; top: 360px; }
  .tag__hole {
    position: absolute;
    left: 50%;
    top: 28px;
    width: 22px;
    height: 22px;
    margin-left: -11px;
    border-radius: 50%;
    background: var(--punch-hole);
  }
  .brand-name {
    position: absolute;
    left: 0;
    right: 0;
    top: 50%;
    transform: translateY(-50%);
    text-align: center;
    font-family: "Cinzel", serif;
    font-weight: 500;
    font-size: 46px;
    line-height: 1.05;
    letter-spacing: 1px;
    color: var(--ink-white);
  }
  .tag__ring {
    position: absolute;
    inset: 16px;
    border: 2px solid var(--gold);
    border-radius: 50%;
  }
  .care-copy {
    position: absolute;
    left: 90px;
    right: 90px;
    top: 82px;
    text-align: center;
    font-family: "Cormorant Garamond", serif;
    font-weight: 500;
    font-size: 17px;
    line-height: 1.32;
    color: var(--ink-white);
  }
  .contact {
    position: absolute;
    left: 0;
    right: 0;
    bottom: 70px;
    text-align: center;
    font-family: "Cinzel", serif;
    font-weight: 500;
    font-size: 13px;
    letter-spacing: 1px;
    line-height: 1.7;
    color: var(--ink-white);
  }
</style>
</head>
<body>
<main class="sheet">
  <section class="tag tag--front">
    <span class="tag__hole"></span>
    <h1 class="brand-name">Lia<br>Montenegro</h1>
  </section>

  <section class="tag tag--back">
    <span class="tag__ring"></span>
    <span class="tag__hole"></span>
    <p class="care-copy">Para aproveitar ao máximo suas peças, acompanhe as dicas de cuidado: guarde os sapatos em local seco e arejado, longe da luz direta do sol. Limpe o couro com pano macio e levemente úmido. Evite contato com água e produtos químicos. Use a embalagem original para armazenar e proteger cada par. Assim sua peça favorita permanece linda por muito mais tempo.</p>
    <div class="contact">
      <p class="contact__phone">(00) 99999 9999</p>
      <p class="contact__email">contato@liamontenegro.com.br</p>
    </div>
  </section>
</main>
</body>
</html>
```